The Velvet Lintel with an elephant incorporated in the background

Target Market(s)

Real estate

Industry/Entity Type

Real Estate

Contact Information for Business Card

On back on want my name & number
In front I want the business name, "the velvet lintel", below to say staging & design

Logo Text

The Velvet Lintel

Font styles to use
Serif

Colors
000000

Requirements
Must have
• I want an elephant behind the writing in gold transperant

```html
<!DOCTYPE html>
<html lang="en">
<head>
<meta charset="utf-8">
<title>The Velvet Lintel — Business Cards</title>
<link rel="stylesheet" href="https://fonts.googleapis.com/css2?family=Federo&family=Josefin+Sans:wght@300;400&family=Tinos&display=swap">
<style>
  :root {
    --page: #d9d9d9;
    --card: #0a0a0a;
    --card-front: #1c1a1b;
    --gold: #d99a1f;
    --gold-deep: #8a5a12;
    --gold-light: #e6b35a;
  }
  html, body {
    margin: 0;
    width: 1200px;
    height: 1200px;
    overflow: hidden;
    background: var(--page);
  }
  .sheet {
    position: relative;
    width: 1200px;
    height: 1200px;
  }
  .card {
    position: absolute;
    left: 220px;
    width: 760px;
    height: 434px;
    box-shadow: 0 6px 18px rgba(0,0,0,0.25);
  }
  .card--front {
    top: 120px;
    background: var(--card-front);
  }
  .card--back {
    top: 640px;
    background: var(--card);
  }
  .brand-name {
    font-family: "Federo", serif;
    color: var(--gold);
    text-transform: uppercase;
    letter-spacing: 0.04em;
    margin: 0;
    font-weight: 400;
  }
  .card--front .brand {
    position: absolute;
    left: 0;
    right: 0;
    top: 150px;
    text-align: center;
  }
  .card--front .brand-name {
    font-size: 44px;
    line-height: 1.15;
  }
  .tagline {
    font-family: "Josefin Sans", sans-serif;
    color: var(--gold);
    font-weight: 300;
    margin: 6px 0 0;
  }
  .card--front .tagline {
    font-size: 20px;
    letter-spacing: 0.3em;
  }
  .card--back .brand {
    position: absolute;
    left: 90px;
    top: 150px;
    width: 300px;
    text-align: center;
  }
  .card--back .brand-name {
    font-size: 30px;
    line-height: 1.25;
  }
  .contact {
    position: absolute;
    left: 150px;
    top: 250px;
    font-family: "Tinos", serif;
    color: var(--gold);
  }
  .contact__name {
    font-size: 28px;
    margin: 0;
    letter-spacing: 0.03em;
  }
  .contact__phone {
    font-size: 18px;
    margin: 10px 0 0 20px;
  }
  .emblem {
    position: absolute;
    left: 430px;
    top: 70px;
    width: 290px;
    height: 200px;
  }
  .emblem svg { display: block; }
  .card--back .tagline {
    position: absolute;
    left: 470px;
    top: 292px;
    font-size: 13px;
    letter-spacing: 0.32em;
    text-transform: uppercase;
  }
</style>
</head>
<body>
<main class="sheet">
  <section class="card card--front">
    <div class="brand">
      <h1 class="brand-name">The Velvet Lintel</h1>
      <p class="tagline">Staging &amp; Design</p>
    </div>
  </section>

  <section class="card card--back">
    <div class="emblem">
      <svg width="290" height="200" viewBox="0 0 290 200" role="img" aria-label="Photograph of an ornate carved brass elephant figurine, trunk raised">
        <defs>
          <radialGradient id="brass" cx="55%" cy="45%" r="60%">
            <stop offset="0%" stop-color="#e6b35a"/>
            <stop offset="60%" stop-color="#b8792a"/>
            <stop offset="100%" stop-color="#5a3a10"/>
          </radialGradient>
        </defs>
        <rect x="0" y="0" width="290" height="200" rx="40" fill="url(#brass)"/>
      </svg>
    </div>
    <p class="tagline">Staging &amp; Design</p>

    <div class="brand">
      <h2 class="brand-name">The Velvet Lintel</h2>
    </div>
    <div class="contact">
      <p class="contact__name">MARCUS HALE</p>
      <p class="contact__phone">T: 555-014-2298</p>
    </div>
  </section>
</main>
</body>
</html>
```